Window Cleaning Leaflet

Hi everyone,

I need a leaflet (couldn't find 'leaflet' as an option when begining this project - so one sided only) to send out to coastal properties in South side Melbourne. The Flyer is aimed at high net individuals, mummies, business people etc who own these properties who don't have time to clean the windows themselves (often multiple levels) and want their home looking fabulous in time for Christmas and NY's celebrations.

I would really love a new and original design for a window washing leaflet. something outside of the norm that 'pops' and makes people feel happy when they look at it.

I guess a point of differentiation is that I'm a female working in a mans industry so appeal to mothers looking for someone who is 'reliable, trustworthy and understanding of peoples needs'.

I have made an outline of what I would like included in the leaflet, so if you could please take a look, feel free to change things around, wording and layout etc. If you can make it sound more professional please do so.

I would like the colours to be 'happy' colours, maybe with a silly season theme?

Overall aesthetically pleasing is a must, I find most window cleaning leaflets fairly mundane and boring, please feel free to think outside the box. The more original the better.

Target Market(s)

People who own large Melbourne homes in affluent suburbs, mainly suburbs with a lot of large coastal properties. Generally owned by high net worth individuals who just don't have tme to clean the windows themselves due to their profession or hectic lifestyles but can afford to pay someone else to do it.

Industry/Entity Type

Window Cleaning

Requirements
Must have
• 1) The name of the business - Tilda’s Glass Gleaming Services
• 2) The coupon special and all details attached:
• Small Homes (up to 12 windows) $120
• Medium Homes (up to 16 windows) $180
• Large Homes (up to 20 windows, 2 storeys) $240
• 20% discount
• *Discount applicable to first time customers only.
• *All services include fly screen, sill and tracks cleaned as well as cobweb removal.
• *Houses with more than 20 windows (or two levels) will have an immediate quote provided upon inspection of the property with 20% discount applied.
• *Tilda’s Glass Gleaming Services are fully insured.
• 3) My contact number - 0418 263 591

```html
<!DOCTYPE html>
<html lang="en">
<head>
<meta charset="utf-8">
<title>Tilda’s Glass Gleaming Services – Leaflet</title>
<link rel="stylesheet" href="https://fonts.googleapis.com/css2?family=Oswald:wght@400;600;700&family=Open+Sans:wght@400;600&display=swap">
<style>
  :root {
    --lime: #d4e021;
    --sky-band: #a9dcf4;
    --orange: #f39a1c;
    --orange-deep: #e8641b;
    --blue: #29a8e0;
    --ink: #222;
    --white: #ffffff;
    --page: #ececec;
  }
  * { box-sizing: border-box; margin: 0; padding: 0; }
  html, body { width: 1010px; height: 1200px; overflow: hidden; background: var(--page); }
  .leaflet {
    position: absolute; left: 61px; top: 30px; width: 888px; height: 1140px;
    background: linear-gradient(to bottom, var(--lime) 0, var(--lime) 300px, var(--white) 540px);
    overflow: hidden; box-shadow: 0 2px 10px rgba(0,0,0,.25);
    font-family: "Open Sans", Arial, sans-serif; color: var(--ink);
  }
  .top-band { position: absolute; left: 0; top: 0; width: 100%; height: 32px; background: var(--sky-band); }
  .bottom-band { position: absolute; left: 0; bottom: 0; width: 100%; height: 12px; background: var(--lime); }
  .hero-photo {
    position: absolute; left: 315px; top: 300px; width: 573px; height: 828px;
    background:
      linear-gradient(to right, rgba(255,255,255,1) 0, rgba(255,255,255,0) 30%),
      linear-gradient(to bottom, rgba(212,224,33,1) 0, rgba(212,224,33,0) 20%),
      linear-gradient(160deg, #bfe3f7 0%, #e9f5fb 35%, #9ccfe9 60%, #f3e2d6 80%, #ffffff 100%);
  }
  .headline {
    position: absolute; left: 44px; top: 46px;
    font-family: "Oswald", "Arial Narrow", sans-serif; font-weight: 600;
    font-size: 80px; line-height: 112px; letter-spacing: -1px; white-space: nowrap;
    color: var(--orange); text-shadow: 3px 3px 0 #3a2a10;
  }
  .headline .mark { color: var(--ink); text-shadow: none; font-weight: 700; }
  .business-name {
    position: absolute; left: 44px; top: 272px;
    font-family: "Oswald", "Arial Narrow", sans-serif; font-weight: 400;
    font-size: 48px; color: var(--blue); white-space: nowrap;
  }
  .intro {
    position: absolute; left: 44px; top: 338px; width: 284px;
    font-size: 15.5px; line-height: 1.38; text-align: justify;
  }
  .intro p { margin-bottom: 18px; }
  .prices { list-style: none; }
  .prices .price { color: var(--orange); }
  .discount-badge {
    position: absolute; left: 141px; top: 644px; width: 176px; height: 176px;
    border-radius: 50%; background: var(--white);
    box-shadow: 0 4px 10px rgba(0,0,0,.3);
    display: flex; align-items: center; justify-content: center;
  }
  .discount-badge .disc {
    width: 148px; height: 148px; border-radius: 50%;
    background: linear-gradient(to bottom, #fbc36a 0, var(--orange) 45%, var(--orange-deep) 100%);
    display: flex; align-items: center; justify-content: center;
    text-align: center; white-space: nowrap;
    font-family: "Oswald", sans-serif; font-weight: 600; font-size: 24px; color: var(--white);
  }
  .terms {
    position: absolute; left: 28px; top: 816px; list-style: none;
    font-size: 15.5px; line-height: 1.36;
  }
  .terms li { position: relative; padding-left: 24px; width: 250px; text-align: justify; }
  .terms li::before {
    content: ""; position: absolute; left: 0; top: 6px; width: 11px; height: 11px;
    border: 2px solid var(--orange);
  }
  .thought-bubble {
    position: absolute; left: 683px; top: 312px; width: 183px; height: 150px;
    border: 5px solid var(--orange); border-radius: 50% 50% 46% 46%;
    background: var(--white);
    display: flex; align-items: center; justify-content: center; text-align: center;
    font-size: 15px; line-height: 1.3; padding: 10px 22px;
  }
  .bubble-tail { position: absolute; left: 760px; top: 455px; }
  .bubble-q {
    position: absolute; left: 846px; top: 462px;
    font-family: "Oswald", sans-serif; font-weight: 700; font-size: 28px; color: var(--orange);
  }
  .call-to-action {
    position: absolute; left: 336px; top: 858px; width: 560px;
    font-family: "Oswald", sans-serif; font-weight: 600; font-size: 34px; line-height: 44px;
    color: var(--orange-deep); transform: rotate(-4deg); transform-origin: left top;
    text-shadow: 1px 1px 0 rgba(255,255,255,.7);
  }
  .phone-ribbon { position: absolute; left: 290px; top: 964px; width: 598px; height: 164px; }
  .phone-ribbon .phone {
    font-family: "Oswald", sans-serif; font-weight: 600; font-size: 40px;
    letter-spacing: 8px; fill: var(--white);
  }
</style>
</head>
<body>
<main class="leaflet">
  <div class="top-band"></div>
  <div class="hero-photo" role="img" aria-label="Smiling woman wiping a sunny window with a yellow cloth and spray bottle"></div>

  <h1 class="headline">Do you need your windows<br>&nbsp;cleaned <span class="mark">?</span></h1>
  <h2 class="business-name">Tilda’s Glass Gleaming Services</h2>

  <section class="intro">
    <p>Tilda understands and wants to help you - enjoy your home looking it’s best before Christmas and NY’s celebrations begin.</p>
    <p>We provide a reliable, professional service, ensuring that your home will sparkle.</p>
    <ul class="prices">
      <li>Small Homes (up to 12 windows) <span class="price">$120</span></li>
      <li>Medium Homes (up to 16 windows) <span class="price">$180</span></li>
      <li>Large Homes (up to 20 windows, 2 storeys) <span class="price">$240</span></li>
    </ul>
  </section>

  <div class="discount-badge"><div class="disc">20% discount</div></div>

  <ul class="terms">
    <li>Discount applicable to first time customers only.</li>
    <li>All services include fly screen, sill and tracks cleaned as well as cobweb removal.</li>
    <li>Houses with more than 20 windows (or two levels) will have an immediate quote provided upon inspection of the property with 20% discount applied.</li>
    <li>Tilda’s Glass Gleaming Services are fully insured.</li>
  </ul>

  <div class="thought-bubble">Are you simply too busy as a hard working parent to do it yourself</div>
  <svg class="bubble-tail" width="40" height="40" viewBox="0 0 40 40" aria-hidden="true">
    <path d="M4 0 L22 34 L26 2 Z" fill="#fff" stroke="#f39a1c" stroke-width="4" stroke-linejoin="round"/>
    <rect x="2" y="-4" width="28" height="6" fill="#fff"/>
  </svg>
  <div class="bubble-q">?</div>

  <p class="call-to-action">Call Tilda today and take advantage<br>&nbsp;&nbsp;of our special introductory offer.</p>

  <svg class="phone-ribbon" viewBox="0 0 620 170" aria-label="Call Tilda on 0418 263 591">
    <defs>
      <linearGradient id="ribbonOrange" x1="0" y1="0" x2="1" y2="0">
        <stop offset="0" stop-color="#e8641b"/>
        <stop offset="1" stop-color="#f7a733"/>
      </linearGradient>
    </defs>
    <path d="M20 78 L612 30 L612 118 L40 166 Q8 150 14 120 Q24 100 20 78 Z" fill="#fff" stroke="#d8d8d8" stroke-width="2"/>
    <path d="M44 84 L596 40 L596 108 L44 152 Z" fill="url(#ribbonOrange)"/>
    <path d="M20 78 Q0 110 24 130 Q40 120 44 100 Z" fill="#e6e6e6"/>
    <text class="phone" x="70" y="138" transform="rotate(-4.5 70 138)">Tilda - 0418 263 591</text>
  </svg>

  <div class="bottom-band"></div>
</main>
</body>
</html>
```